Letterhead for clinic notes, test reports, and business cards

I need business card and letterheads for a medical clinic with the following:
1- Business cards. The back should allow for space for date and time of next appointments (few lines would do)
2- Letterhead for clinic notes
3- Letterhead for test reports.

Feel free to use whats included for examples. I value creativity so be creative.

Target Market(s)

Patients, referring physicians.

Industry/Entity Type

Health Care

Requirements
Must have
• Must use current logo.
• Must look good on white background
• Letterhead and reports must look good faxed.
• Please use themes of the current logo. Another possible color to use is grey as well (www.brambleveincare.org - use the font color in the text of that website)

```html
<!DOCTYPE html>
<html lang="en">
<head>
<meta charset="utf-8">
<title>Lakeshore Heart Centre – Test Report Letterhead</title>
<link href="https://fonts.googleapis.com/css2?family=Open+Sans:ital,wght@0,400;0,600;0,700;1,400;1,700&family=Crimson+Text&display=swap" rel="stylesheet">
<style>
  :root{
    --bg:#dfe7ef;
    --paper:#ffffff;
    --navy:#1a2f6e;
    --blue:#1f5fae;
    --grey:#9a9a9a;
    --text:#333333;
    --soft:#777777;
    --red:#b0201e;
    --rule:#b8b8b8;
  }
  *{box-sizing:border-box;margin:0;padding:0}
  html,body{width:1200px;height:784px;overflow:hidden;background:var(--bg)}
  body{font-family:"Open Sans",Arial,sans-serif;color:var(--text)}
  .page{position:absolute;left:314px;top:22px;width:572px;height:740px;background:var(--paper);box-shadow:0 2px 8px rgba(0,0,0,.12);overflow:hidden}
  .abs{position:absolute}
  .header-bar-grey{left:0;top:30px;width:70px;height:7px;background:var(--grey)}
  .header-bar-blue{left:210px;top:60px;width:362px;height:6px;background:linear-gradient(90deg,var(--blue),var(--navy))}
  .brand{left:80px;top:24px;width:125px}
  .brand-name{display:flex;align-items:center;gap:6px;font-size:12px;font-weight:700;color:var(--navy);line-height:1.15}
  .brand-dot{width:12px;height:12px;border-radius:50%;background:var(--navy);flex:none}
  .provider{left:80px;top:56px;font-size:6px;color:var(--soft);font-style:italic}
  .label{font-size:6.5px;font-weight:700;line-height:1.55}
  .rule{height:1px;background:var(--rule)}
  .title{left:200px;top:196px;font-size:12px;font-weight:700;font-style:italic}
  table.results{left:110px;top:218px;border-collapse:collapse;font-size:6px}
  .results th,.results td{border:1px solid var(--rule);padding:1px 4px;text-align:left;font-weight:400}
  .results th{font-weight:600}
  .box{display:inline-block;width:5px;height:5px;border:1px solid #888;margin-right:2px;vertical-align:middle}
  .note{font-size:6.5px;line-height:1.5}
  .note-head{color:var(--red);font-weight:700;font-style:italic;font-size:7px}
  .sign{font-size:7px;font-weight:700;font-style:italic}
  .script-name{left:330px;top:640px;font-family:"Crimson Text",Georgia,serif;color:var(--red);font-size:17px}
  .prepared{left:330px;top:664px;font-size:6.5px}
  .footer-band{left:0;top:728px;width:572px;height:12px;background:linear-gradient(90deg,var(--navy),var(--blue))}
  .footer{left:18px;top:708px;width:540px;display:flex;justify-content:space-between;font-size:7px;color:var(--soft)}
  .footer span{display:flex;align-items:center;gap:4px}
  .footer svg{flex:none}
</style>
</head>
<body>
<div class="page">
  <div class="abs header-bar-grey"></div>
  <div class="abs brand"><div class="brand-name"><span class="brand-dot"></span>Lakeshore Heart Centre</div></div>
  <div class="abs provider">Provider No. 0000000X &nbsp;|&nbsp; ABN 00 000 000 000</div>
  <div class="abs header-bar-blue"></div>

  <div class="abs label" style="left:30px;top:84px">Name<br>Exam ID<br>Exam Date</div>
  <div class="abs label" style="left:210px;top:84px">Med Rec No.<br>Date of Birth<br>Referred By<br>V. S. History</div>
  <div class="abs label" style="left:380px;top:84px">Age<br><br>Sex</div>
  <div class="abs label" style="left:470px;top:84px">Admission<br>Room #<br>Prior Exam:<br>Limited: &nbsp;No</div>
  <div class="abs label" style="left:30px;top:128px">Risk Factors</div>
  <div class="abs label" style="left:30px;top:150px">Medications</div>
  <div class="abs label" style="left:210px;top:150px">Reason for Study</div>
  <div class="abs rule" style="left:30px;top:170px;width:512px"></div>

  <div class="abs title">Aneurysm Survey</div>
  <table class="abs results">
    <tr><th>Vessel</th><th colspan="3">Right</th><th colspan="3">Left</th></tr>
    <tr><th></th><th>A-P</th><th>Lat</th><th>Thrombus</th><th>A-P</th><th>Lat</th><th>Thrombus</th></tr>
    <tr><td>Prox CFA</td><td>.95 cm.</td><td>.74 cm.</td><td><span class="box"></span>Present</td><td>cm.</td><td>cm.</td><td><span class="box"></span>Present</td></tr>
    <tr><td>Mid CFA</td><td>.85 cm.</td><td>.95 cm.</td><td><span class="box"></span>Present</td><td>cm.</td><td>cm.</td><td><span class="box"></span>Present</td></tr>
    <tr><td>Distal CFA</td><td>.74 cm.</td><td>.84 cm.</td><td><span class="box"></span>Present</td><td>cm.</td><td>cm.</td><td><span class="box"></span>Present</td></tr>
    <tr><td>Prox SFA</td><td>.87 cm.</td><td>.99 cm.</td><td><span class="box"></span>Present</td><td>cm.</td><td>cm.</td><td><span class="box"></span>Present</td></tr>
    <tr><td>Mid SFA</td><td>2.5 cm.</td><td>2.6 cm.</td><td><span class="box"></span>Present</td><td>cm.</td><td>cm.</td><td><span class="box"></span>Present</td></tr>
    <tr><td>Distal SFA</td><td>.95 cm.</td><td>.94 cm.</td><td><span class="box"></span>Present</td><td>cm.</td><td>cm.</td><td><span class="box"></span>Present</td></tr>
    <tr><td>Prox POP</td><td>.65 cm.</td><td>.54 cm.</td><td><span class="box"></span>Present</td><td>cm.</td><td>cm.</td><td><span class="box"></span>Present</td></tr>
    <tr><td>Mid POP</td><td>.54 cm.</td><td>.54 cm.</td><td><span class="box"></span>Present</td><td>cm.</td><td>cm.</td><td><span class="box"></span>Present</td></tr>
    <tr><td>Distal POP</td><td>.68 cm.</td><td>.68 cm.</td><td><span class="box"></span>Present</td><td>cm.</td><td>cm.</td><td><span class="box"></span>Present</td></tr>
  </table>
  <div class="abs note" style="left:30px;top:400px;width:500px">Noninvasive evaluation of the lower extremity native arteries with B-mode imaging, color Doppler, spectral Doppler analysis and representative diameter measurements.</div>
  <div class="abs note" style="left:30px;top:428px;width:500px"><span class="note-head">Interpretation:</span><br>The maximum diameter measurement of the right superficial femoral artery is 2.6 cm.</div>
  <div class="abs note" style="left:30px;top:456px;width:500px"><span class="note-head">Impression:</span><br>Aneurysm noted on the right superficial femoral artery.</div>
  <div class="abs rule" style="left:30px;top:488px;width:512px"></div>

  <div class="abs sign" style="left:30px;top:540px">Daniel R Hayes, M.D.</div>
  <div class="abs sign" style="left:260px;top:540px">9/8/2010</div>
  <div class="abs label" style="left:330px;top:560px;font-style:italic">Performed By:<br>Transcribed:</div>

  <div class="abs script-name">Lakeshore Heart Centre</div>
  <div class="abs prepared">Report Prepared by Lakeshore Heart Centre</div>

  <div class="abs footer">
    <span><svg width="8" height="8" viewBox="0 0 8 8"><circle cx="4" cy="4" r="3.5" fill="none" stroke="#1a2f6e"/><circle cx="4" cy="3.5" r="1.2" fill="#1a2f6e"/></svg>118 Maple Crest Road, Suite 4, Riverton ON K2P1L8</span>
    <span><svg width="8" height="8" viewBox="0 0 8 8"><circle cx="4" cy="4" r="3.5" fill="none" stroke="#1a2f6e"/><rect x="3" y="2" width="2" height="4" rx=".6" fill="#1a2f6e"/></svg>555.201.4417</span>
    <span><svg width="8" height="8" viewBox="0 0 8 8"><circle cx="4" cy="4" r="3.5" fill="none" stroke="#1a2f6e"/><rect x="2" y="3" width="4" height="2.5" fill="#1a2f6e"/></svg>555.201.4418</span>
    <span><svg width="8" height="8" viewBox="0 0 8 8"><circle cx="4" cy="4" r="3.5" fill="none" stroke="#1a2f6e"/><path d="M2 3h4v2.5H2z M2 3l2 1.3L6 3" fill="none" stroke="#1a2f6e" stroke-width=".7"/></svg>contact@lakeshoreheart.org</span>
  </div>
  <div class="abs footer-band"></div>
</div>
</body>
</html>
```